Corvane Solutions Website

Corvane Solutions (CS) provide Analytics & Enterprise Performance Management (EPM) advisory & consultancy services. We are passionate about data and making a difference for our clients by working in partnership with them, helping them on their journey to becoming an Corvane Solution. We deliver insights which give our clients a competitive edge and a much deeper understanding of their organisation.

We need a website which shows who we are, what we do and how we do it.

www.corvane-solutions.com is our very basic website at the moment. We want to completely revamp it with a corporate look

```html
<!DOCTYPE html>
<html lang="en">
<head>
<meta charset="utf-8">
<title>Corvane Solutions – Data Analytics &amp; EPM Consulting</title>
<link href="https://fonts.googleapis.com/css2?family=Fira+Sans:wght@500;600;700&family=Roboto:wght@400;500;700&display=swap" rel="stylesheet">
<style>
:root{
  --navy:#2d5774;
  --navy-deep:#234a64;
  --ink:#2a5470;
  --orange:#e0834f;
  --text:#555b62;
  --muted:#8a8f95;
  --line:#d9dde1;
  --white:#ffffff;
}
*{box-sizing:border-box;margin:0;padding:0}
html,body{width:1200px;height:3447px;overflow:hidden}
body{position:relative;background:var(--white);font-family:'Roboto',sans-serif;color:var(--text)}
.abs{position:absolute}
h1,h2,h3,h4,.heading{font-family:'Fira Sans',sans-serif;font-weight:700}

/* header & hero */
.hero{left:0;top:0;width:1200px;height:676px;background:var(--navy)}
.logo{display:flex;align-items:center;gap:12px;color:var(--white)}
.logo-dot{width:48px;height:48px;border-radius:50%;border:7px solid var(--white)}
.logo-name{font-family:'Fira Sans',sans-serif;font-weight:600;font-size:23px;line-height:25px;letter-spacing:.5px}
.nav{left:485px;top:46px;display:flex;gap:35px;font-size:14px;color:var(--white)}
.nav .active{color:var(--orange)}
.btn{display:flex;align-items:center;justify-content:center;background:var(--orange);color:var(--white);border-radius:30px;font-size:14px;font-weight:500}
.tag{left:86px;top:217px;width:220px;height:45px;border:1.5px solid var(--orange);border-radius:4px;color:var(--orange);font-size:18px;display:flex;align-items:center;justify-content:center}
.hero-title{left:84px;top:278px;font-size:42px;line-height:47px;color:var(--white);font-weight:600}
.hero-text{left:87px;top:386px;width:480px;font-size:16px;line-height:23px;color:var(--white)}
.photo{background:linear-gradient(135deg,#c9d4dc,#7f97a8 55%,#44606f)}
.photo-frame{left:460px;top:491px;width:279px;height:218px;background:var(--white)}

/* labels */
.eyebrow{display:flex;align-items:center;gap:12px;color:var(--orange);font-size:14px;font-weight:500}
.eyebrow::after{content:"";width:28px;height:2px;background:var(--orange)}
.eyebrow.center::before{content:"";width:28px;height:2px;background:var(--orange)}
.section-title{color:var(--ink);font-size:38px;line-height:42px}

/* about */
.about-card{left:261px;top:839px;width:852px;height:468px;background:var(--white);box-shadow:0 4px 22px rgba(0,0,0,.08)}
.about-text{font-size:14px;line-height:21px;color:var(--text)}
.btn-outline{display:flex;align-items:center;justify-content:center;border:1.5px solid var(--orange);color:var(--orange);border-radius:30px;font-size:14px}
.partner-badge{left:776px;top:1200px;width:154px;height:34px;display:flex;align-items:center;gap:10px}

/* services */
.services-band{left:0;top:1782px;width:1200px;height:590px;background:linear-gradient(180deg,var(--navy),var(--navy-deep))}
.card{width:325px;height:366px;background:var(--white);box-shadow:0 4px 20px rgba(0,0,0,.08);padding:40px 34px}
.card-icon{width:78px;height:78px;border-radius:50%;background:var(--orange);display:flex;align-items:center;justify-content:center}
.card h3{margin-top:22px;color:var(--ink);font-size:19px;line-height:26px;font-weight:600}
.card p{margin-top:14px;font-size:13.5px;line-height:21px}
.learn{margin-top:22px;color:var(--ink);font-size:14px;font-weight:700}

/* process */
.step-num{width:53px;height:53px;border-radius:50%;background:var(--orange)}
.step-num span{position:absolute;left:30px;top:18px;font-family:'Fira Sans',sans-serif;font-weight:700;font-size:32px;color:var(--white)}
.step-title{font-size:21px;line-height:28px;color:var(--white);font-weight:600}
.step-text{width:290px;font-size:14px;line-height:23px;color:var(--white)}

/* contact */
.field{border:1px solid var(--line);font-size:13.5px;color:var(--muted);padding:12px 14px}

/* footer */
.footer{left:0;top:3044px;width:1200px;height:403px;background:var(--navy)}
.footer h4{font-size:21px;color:var(--white);font-weight:600}
.footer-list{list-style:none;font-size:13.5px;color:var(--white)}
.footer-list li{height:33.5px}
.footer-list li::before{content:"»";color:#9fb3c2;margin-right:14px}
.social{width:44px;height:43px;background:#5d7e95}
.copyright{left:0;top:3396px;width:1200px;text-align:center;font-size:13.5px;color:var(--white)}
.copyright b{color:var(--orange);font-weight:400}
</style>
</head>
<body>

<!-- hero -->
<section class="abs hero"></section>
<div class="abs logo" style="left:86px;top:24px">
  <div class="logo-dot"></div>
  <div class="logo-name">CORVANE<br>SOLUTIONS</div>
</div>
<nav class="abs nav">
  <span class="active">Home</span><span>Who We Are</span><span>What We Do</span><span>How We Do</span><span>Contact</span>
</nav>
<a class="abs btn" style="left:982px;top:33px;width:130px;height:45px">Get Started</a>

<div class="abs tag">Corvane Solutions</div>
<h1 class="abs hero-title">Data Analytics &amp;<br>Epm Consulting Services</h1>
<p class="abs hero-text">CS are a Data Analytics &amp; EPM company, specialising in the implementation and support of Business Intelligence, EPM and Data Analytics business solutions, both in the Cloud and on-premise.</p>
<a class="abs btn" style="left:86px;top:499px;width:156px;height:46px;gap:12px">Get Started
  <svg width="22" height="22" viewBox="0 0 22 22"><circle cx="11" cy="11" r="9.5" fill="none" stroke="#fff" stroke-width="1.5"/><path d="M6.5 11h8M11.5 7.5l3.5 3.5-3.5 3.5" fill="none" stroke="#fff" stroke-width="1.5"/></svg>
</a>
<div class="abs photo" role="img" aria-label="Laptop and monitor showing business analytics charts" style="left:640px;top:122px;width:560px;height:459px"></div>
<div class="abs photo-frame"></div>
<div class="abs photo" role="img" aria-label="Team meeting around a table viewed from above" style="left:473px;top:504px;width:254px;height:205px;background:linear-gradient(135deg,#e6dcc9,#9a8f80 50%,#3e4752)"></div>

<!-- about -->
<div class="abs about-card"></div>
<div class="abs photo" role="img" aria-label="Hand with stylus over a tablet displaying analysis data" style="left:86px;top:886px;width:439px;height:376px;background:linear-gradient(135deg,#1c2b8a,#2f6ad8 50%,#0d1440)"></div>
<div class="abs eyebrow" style="left:595px;top:901px">Who We Are</div>
<h2 class="abs section-title" style="left:595px;top:930px;font-size:36px">Welcome to<br>Corvane Solutions</h2>
<p class="abs about-text" style="left:595px;top:1028px;width:460px">Corvane Solutions is an exciting start-up in the Data Analytics and EPM space.&nbsp; Founded in 2019, CS specialise in the implementation and support of BI, EPM and Data Analytics business solutions, both in the Cloud and on-premise.</p>
<p class="abs about-text" style="left:595px;top:1128px;width:470px">Call us on 01 555 0142 or email: info@corvane-solutions.com for more information</p>
<a class="abs btn-outline" style="left:595px;top:1193px;width:158px;height:47px">Get Free Quote</a>
<div class="abs partner-badge"><div style="width:84px;height:16px;background:#d7362b;border-radius:2px"></div><div style="width:2px;height:34px;background:#222"></div><div style="width:50px;height:16px;background:#3a3a3a;border-radius:2px"></div></div>

<!-- services -->
<div class="abs eyebrow" style="left:84px;top:1423px">What We Do</div>
<h2 class="abs section-title" style="left:84px;top:1451px">Our Services</h2>
<p class="abs about-text" style="left:589px;top:1427px;width:525px;font-size:13.5px">We are passionate about data and making a difference for our clients by working in partnership with them, helping them on their journey to becoming an Corvane Solution.</p>
<div class="abs services-band"></div>

<article class="abs card" style="left:86px;top:1519px">
  <div class="card-icon"><svg width="38" height="38" viewBox="0 0 38 38" fill="none" stroke="#fff" stroke-width="1.6"><rect x="12" y="6" width="18" height="12" rx="2"/><path d="M17 12h8M5 28l8-3h8l6-4M5 33h14l12-7"/></svg></div>
  <h3>Advise &amp;<br>Architect services</h3>
  <p>Helping our customers understand the art of the possible and safeguarding their investments by overseeing implementations.</p>
  <div class="learn">Learn More &nbsp;»</div>
</article>
<article class="abs card" style="left:436px;top:1519px">
  <div class="card-icon"><svg width="38" height="38" viewBox="0 0 38 38" fill="none" stroke="#fff" stroke-width="1.6"><rect x="6" y="8" width="26" height="24"/><path d="M12 26l14-14M12 26l1-5 4 4z"/></svg></div>
  <h3>Design<br>&amp; Implement</h3>
  <p>Working with the project management team, through each stage of the project, with clearly defined deliverables and well exercised plans to deliver them.</p>
  <div class="learn">Learn More &nbsp;»</div>
</article>
<article class="abs card" style="left:788px;top:1519px">
  <div class="card-icon"><svg width="38" height="38" viewBox="0 0 38 38" fill="none" stroke="#fff" stroke-width="1.6"><circle cx="19" cy="19" r="12"/><path d="M15 15l-4 4 4 4M23 15l4 4-4 4M21 13l-4 12"/></svg></div>
  <h3>Optimise &amp;<br>Manage</h3>
  <p>Our Managed Services delivers proactive, on-demand support for EPM and Data Analytics environments</p>
  <div class="learn">Learn More &nbsp;»</div>
</article>

<!-- process -->
<div class="abs eyebrow center" style="left:0;top:2002px;width:1200px;justify-content:center">How We Do It</div>
<h2 class="abs section-title" style="left:0;top:2034px;width:1200px;text-align:center;color:#fff">Our Working Process</h2>

<div class="abs step-num" style="left:91px;top:2110px"><span>1</span></div>
<div class="abs step-title" style="left:165px;top:2108px">Lorem Ipsum<br>Step1</div>
<div class="abs step-num" style="left:443px;top:2110px"><span>2</span></div>
<div class="abs step-title" style="left:516px;top:2108px">Lorem Ipsum<br>Step2</div>
<div class="abs step-num" style="left:793px;top:2110px"><span>3</span></div>
<div class="abs step-title" style="left:867px;top:2108px">Lorem Ipsum<br>Step 3</div>
<svg class="abs" style="left:315px;top:2125px" width="112" height="24" viewBox="0 0 112 24" fill="none" stroke="#8ea6b8" stroke-width="2"><path d="M2 18C35 6 70 6 104 12" stroke-dasharray="7 5"/><path d="M98 7l7 5-7 5"/></svg>
<svg class="abs" style="left:666px;top:2125px" width="112" height="24" viewBox="0 0 112 24" fill="none" stroke="#8ea6b8" stroke-width="2"><path d="M2 18C35 6 70 6 104 12" stroke-dasharray="7 5"/><path d="M98 7l7 5-7 5"/></svg>
<p class="abs step-text" style="left:91px;top:2192px">Lorem ipsum dolor sit amet, consectetur adipiscing elit. Aenean venenatis leo quis mauris efficitur ultrices.</p>
<p class="abs step-text" style="left:443px;top:2192px">Lorem ipsum dolor sit amet, consectetur adipiscing elit. Aenean venenatis leo quis mauris efficitur ultrices.</p>
<p class="abs step-text" style="left:793px;top:2192px">Lorem ipsum dolor sit amet, consectetur adipiscing elit. Aenean venenatis leo quis mauris efficitur ultrices.</p>

<!-- contact -->
<div class="abs eyebrow" style="left:85px;top:2489px">Contact Us</div>
<h2 class="abs section-title" style="left:85px;top:2517px">Get in Touch</h2>
<p class="abs about-text" style="left:86px;top:2568px">Contact us to discuss your business needs</p>
<div class="abs field" style="left:86px;top:2613px;width:243px;height:42px">First name*</div>
<div class="abs field" style="left:342px;top:2613px;width:244px;height:42px">Last name*</div>
<div class="abs field" style="left:86px;top:2672px;width:243px;height:42px">Phone number*</div>
<div class="abs field" style="left:342px;top:2672px;width:244px;height:42px">Email*</div>
<div class="abs field" style="left:86px;top:2731px;width:500px;height:103px">Message</div>
<a class="abs btn" style="left:86px;top:2857px;width:107px;height:40px">Send Now</a>
<div class="abs photo" role="img" aria-label="Smiling businesswoman in an office with colleagues behind" style="left:760px;top:2491px;width:353px;height:352px;border-radius:50%;background:linear-gradient(135deg,#dfe6ec,#a9b8c4 55%,#3a4650)"></div>
<div class="abs" style="left:676px;top:2670px;width:248px;height:248px;border-radius:50%;background:#fff;box-shadow:0 4px 18px rgba(0,0,0,.12)"></div>
<div class="abs photo" role="img" aria-label="Laptop screen with analytics dashboard" style="left:688px;top:2682px;width:224px;height:224px;border-radius:50%;background:linear-gradient(135deg,#c9d6e6,#6f88b3 55%,#2b355e)"></div>

<!-- footer -->
<footer class="abs footer"></footer>
<div class="abs logo" style="left:87px;top:3117px;gap:10px">
  <div class="logo-dot" style="width:42px;height:42px;border-width:6px"></div>
  <div class="logo-name" style="font-size:15.5px;line-height:17px">CORVANE<br>SOLUTIONS</div>
</div>
<p class="abs" style="left:88px;top:3180px;width:275px;font-size:13.5px;line-height:21px;color:#fff">We deliver insights which give our clients a competitive edge and a much deeper understanding of their organisation.</p>
<div class="abs social" style="left:86px;top:3258px"></div>
<div class="abs social" style="left:143px;top:3258px"></div>

<h4 class="abs" style="left:417px;top:3114px;color:#fff;font-size:21px;font-weight:600">Main Menu</h4>
<ul class="abs footer-list" style="left:418px;top:3174px"><li>Home</li><li>Who We Are</li><li>What We Do</li><li>How We Do</li><li>Contact</li></ul>
<h4 class="abs" style="left:597px;top:3114px;color:#fff;font-size:21px;font-weight:600">Our Services</h4>
<ul class="abs footer-list" style="left:598px;top:3174px"><li>Advise &amp; Architect</li><li>Design &amp; Implement</li><li>Optimise &amp; Manage</li></ul>
<h4 class="abs" style="left:823px;top:3114px;color:#fff;font-size:21px;font-weight:600">Contact</h4>
<div class="abs" style="left:824px;top:3174px;width:320px;font-size:13.5px;line-height:21px;color:#fff">
  <p style="margin-bottom:12px">Call : 01 555 0142</p>
  <p style="margin-bottom:12px">Email : info@corvane-solutions.com</p>
  <p>Location : 14 Harbour Row, Millbrook, Dublin 4, D04 QX17</p>
</div>
<div class="abs" style="left:0;top:3378px;width:1200px;height:1px;background:rgba(255,255,255,.15)"></div>
<p class="abs copyright">Copyright © 2022 <b>Corvane-Solutions</b>.All Rights Reserved.</p>

</body>
</html>
```